Fast-casual chicken restaurant Brisket Barn needs a catering menu design

We need a catering menu designed for Brisket Barn. We are looking to design a 24x36in landscape menu board for our new catering menu. The catering memo attached includes our catering menu and Brisket Barn branding. More information about our brand can be found at https://brisketbarn-eats.example/.

```html
<!DOCTYPE html>
<html lang="en">
<head>
<meta charset="utf-8">
<title>Brisket Barn Catering Menu</title>
<link href="https://fonts.googleapis.com/css2?family=Montserrat:ital,wght@0,400;0,500;0,600;0,700;0,800;0,900;1,800;1,900&display=swap" rel="stylesheet">
<style>
  :root {
    --yellow: #fbc92d;
    --yellow-light: #fdd23f;
    --red: #d9412f;
    --red-dark: #c93626;
    --white: #ffffff;
    --navy: #2d3f78;
  }
  * { margin: 0; padding: 0; box-sizing: border-box; }
  html, body { width: 1200px; height: 800px; overflow: hidden; }
  body {
    font-family: "Montserrat", sans-serif;
    background: var(--yellow);
    position: relative;
    color: var(--red);
  }
  .board { position: absolute; inset: 0; overflow: hidden; }
  .abs { position: absolute; }

  .photo-top {
    left: 0; top: 0; width: 1200px; height: 124px;
    background: linear-gradient(90deg, #c7873a 0%, #9a5f30 18%, #6e3d22 30%, #8a5a34 42%, #d49a4c 50%, #8a5a34 58%, #6e3d22 70%, #9a5f30 82%, #c7873a 100%);
  }
  .photo-side-left {
    left: 0; top: 100px; width: 74px; height: 150px;
    background: linear-gradient(180deg, #c98a3a, rgba(251,201,45,0));
  }
  .photo-side-right {
    right: 0; top: 100px; width: 74px; height: 150px;
    background: linear-gradient(180deg, #c98a3a, rgba(251,201,45,0));
  }
  .photo-tray-center {
    left: 486px; top: 0; width: 228px; height: 184px;
    background: radial-gradient(circle at 50% 45%, #b8501f, #d99a45 70%, #eee 96%);
    border-radius: 0 0 10px 10px;
  }
  .photo-plate-bl {
    left: -40px; top: 706px; width: 270px; height: 150px;
    background: radial-gradient(circle at 50% 60%, #c2421f, #d9753a 70%, #f4f1ea 95%);
    border-radius: 24px; transform: rotate(-8deg);
  }
  .photo-dip {
    left: 244px; top: 688px; width: 94px; height: 94px; border-radius: 50%;
    background: radial-gradient(circle, #fbfbf6 55%, #d8d8d2 100%);
  }
  .photo-plate-center {
    left: 348px; top: 680px; width: 300px; height: 190px; border-radius: 50%;
    background: radial-gradient(circle, #c07a32, #9a5424 60%, #2a2a2a 78%);
  }
  .photo-tray-br {
    left: 700px; top: 662px; width: 324px; height: 170px; border-radius: 18px;
    background: radial-gradient(circle at 50% 60%, #a13a1c, #c8672b 70%, #f4f1ea 95%);
    transform: rotate(-4deg);
  }
  .photo-plate-right {
    left: 1068px; top: 576px; width: 230px; height: 260px; border-radius: 50%;
    background: radial-gradient(circle, #c2421f, #b5331c 60%, #222 76%);
  }

  .title {
    left: 0; top: 186px; width: 1200px; text-align: center;
    font-weight: 800; font-size: 72px; letter-spacing: 4px; color: var(--red);
    line-height: 1;
  }

  .section-head {
    font-weight: 800; font-size: 21px; letter-spacing: 2.2px; color: var(--white);
    line-height: 1;
  }
  .rule { height: 3px; background: var(--white); }

  .note {
    left: 130px; top: 285px; font-size: 8.5px; font-weight: 700; font-style: italic;
    color: var(--navy); letter-spacing: 0.4px;
  }
  .note::before { content: "▸ "; font-style: normal; }

  .package {
    top: 304px; width: 150px; height: 184px;
    background: linear-gradient(90deg, rgba(253,214,70,0.9), rgba(251,201,45,0.4));
    box-shadow: -6px 6px 10px rgba(170,120,0,0.18);
    padding: 22px 0 0 27px;
  }
  .package-notch { position: absolute; left: 0; top: 20px; }
  .package-option { font-size: 9.5px; letter-spacing: 1.6px; font-weight: 500; }
  .package-name { font-size: 23px; font-weight: 800; line-height: 1; margin-top: 3px; }
  .package-items {
    list-style: none; margin-top: 16px; font-size: 13.5px; font-weight: 500; line-height: 13.9px;
  }
  .package-price {
    position: absolute; left: 27px; top: 170px; font-size: 12px; letter-spacing: 1.8px; font-weight: 500;
  }

  .meal { top: 296px; width: 129px; height: 198px; border-radius: 4px; overflow: hidden; background: var(--red); }
  .meal-title {
    height: 56px; background: var(--white); text-align: center;
    font-weight: 800; font-size: 22px; line-height: 21px; padding-top: 7px; position: relative;
    letter-spacing: -0.3px;
  }
  .meal-title svg { position: absolute; left: 55px; bottom: -9px; }
  .meal-body {
    color: var(--white); text-align: center; font-size: 12.8px; font-weight: 500; line-height: 13.8px;
    list-style: none; position: absolute; left: 0; width: 129px;
  }
  .meal-price {
    position: absolute; left: 0; width: 129px; top: 173px; text-align: center;
    color: var(--white); font-size: 11.5px; letter-spacing: 1.6px; font-weight: 500;
  }

  .count {
    font-weight: 900; font-style: italic; font-size: 18px; line-height: 1; color: var(--red);
  }
  .count-price { font-size: 11px; font-weight: 500; margin-top: 2px; }

  .side-name { font-weight: 800; font-size: 20px; line-height: 20px; }
  .side-size { font-size: 11.5px; font-weight: 500; margin-top: 3px; }
  .side-price { font-size: 11px; letter-spacing: 1.5px; font-weight: 500; }

  .learn-more {
    left: 682px; top: 718px; width: 404px; height: 32px;
    background: var(--white); border: 3px solid var(--navy); border-radius: 4px;
    color: var(--navy); font-size: 12.6px; letter-spacing: 0.6px; font-weight: 500;
    display: flex; align-items: center; justify-content: center; white-space: nowrap;
    text-decoration: none;
  }
  .learn-more strong { font-weight: 800; margin-left: 5px; }
  .cursor { left: 1074px; top: 736px; }
</style>
</head>
<body>
<main class="board">
  <div class="abs photo-top" role="img" aria-label="Overhead photo of platters of wings, ribs and tenders on a wooden table"></div>
  <div class="abs photo-side-left" role="img" aria-label="Onion rings at the board edge"></div>
  <div class="abs photo-side-right" role="img" aria-label="Onion rings at the board edge"></div>
  <div class="abs photo-tray-center" role="img" aria-label="Tray of fried chicken tenders"></div>

  <h1 class="abs title">CATERING MENU</h1>

  <h2 class="abs section-head" style="left:130px;top:262px;">PACKAGES</h2>
  <div class="abs rule" style="left:296px;top:272px;width:318px;"></div>
  <p class="abs note">A MINIMUM OF 10 PEOPLE ARE NEEDED FOR THE PER PERSON DEALS</p>

  <section class="abs package" style="left:150px;">
    <svg class="package-notch" width="14" height="34" viewBox="0 0 14 34"><polygon points="0,0 14,17 0,34" fill="#e0a91f"/></svg>
    <div class="package-option">OPTION 1</div>
    <div class="package-name">SNACK</div>
    <ul class="package-items"><li>2 TENDERS</li><li>SAUCE</li><li>DRESSING</li><li>1 REG SIDE</li></ul>
    <div class="package-price">$7.00/PERSON</div>
  </section>
  <section class="abs package" style="left:309px;">
    <svg class="package-notch" width="14" height="34" viewBox="0 0 14 34"><polygon points="0,0 14,17 0,34" fill="#e0a91f"/></svg>
    <div class="package-option">OPTION 2</div>
    <div class="package-name">MEAL</div>
    <ul class="package-items"><li>2 TENDERS</li><li>3 WINGS</li><li>SAUCE</li><li>DRESSING</li><li>1 REG SIDE</li><li>12OZ DRINK</li></ul>
    <div class="package-price">$11.00/PERSON</div>
  </section>
  <section class="abs package" style="left:465px;">
    <svg class="package-notch" width="14" height="34" viewBox="0 0 14 34"><polygon points="0,0 14,17 0,34" fill="#e0a91f"/></svg>
    <div class="package-option">OPTION 3</div>
    <div class="package-name">FEAST</div>
    <ul class="package-items"><li>2 TENDERS</li><li>6 WINGS</li><li>SAUCE</li><li>DRESSING</li><li>1 REG SIDE</li><li>20OZ DRINK</li></ul>
    <div class="package-price">$15.00/PERSON</div>
  </section>

  <h2 class="abs section-head" style="left:670px;top:262px;">MEALS</h2>
  <div class="abs rule" style="left:778px;top:272px;width:304px;"></div>

  <section class="abs meal" style="left:671px;">
    <div class="meal-title">FAMILY<br>MEAL<svg width="20" height="10" viewBox="0 0 20 10"><polygon points="0,0 20,0 10,10" fill="#fff"/></svg></div>
    <ul class="meal-body" style="top:89px;"><li>12 TENDERS</li><li>SAUCES</li><li>DRESSING</li><li>LARGE SIDE</li><li>2L</li></ul>
    <div class="meal-price">$24.99</div>
  </section>
  <section class="abs meal" style="left:813px;">
    <div class="meal-title">PARTY<br>PACK<svg width="20" height="10" viewBox="0 0 20 10"><polygon points="0,0 20,0 10,10" fill="#fff"/></svg></div>
    <ul class="meal-body" style="top:71px;"><li>20 TENDERS</li><li>30 WINGS</li><li>SAUCES</li><li>2 PARTY SIDES</li><li>2 PARTY SALADS</li><li>DRESSINGS</li><li>2 2L</li></ul>
    <div class="meal-price" style="top:171px;">$75.99</div>
  </section>
  <section class="abs meal" style="left:954px;">
    <div class="meal-title">AIRCRAFT<br>CARRIER<svg width="20" height="10" viewBox="0 0 20 10"><polygon points="0,0 20,0 10,10" fill="#fff"/></svg></div>
    <ul class="meal-body" style="top:71px;"><li>20 TENDERS</li><li>60 WINGS</li><li>SAUCES</li><li>2 PARTY SIDES</li><li>2 PARTY SALADS</li><li>DRESSINGS</li><li>2 2L</li></ul>
    <div class="meal-price">$155.99</div>
  </section>

  <h2 class="abs section-head" style="left:130px;top:517px;">WINGS</h2>
  <div class="abs rule" style="left:238px;top:527px;width:58px;"></div>
  <h2 class="abs section-head" style="left:309px;top:517px;">TENDERS</h2>
  <div class="abs rule" style="left:447px;top:527px;width:77px;"></div>
  <h2 class="abs section-head" style="left:538px;top:517px;">SIDES</h2>
  <div class="abs rule" style="left:632px;top:527px;width:450px;"></div>

  <div class="abs" style="left:135px;top:554px;"><div class="count">50 WINGS</div><div class="count-price">$7.00</div></div>
  <div class="abs" style="left:135px;top:597px;"><div class="count">75 WINGS</div><div class="count-price">$XX.XX</div></div>
  <div class="abs" style="left:135px;top:638px;"><div class="count">100 WINGS</div><div class="count-price">$XX.XX</div></div>

  <div class="abs" style="left:310px;top:554px;"><div class="count">30 TENDERS</div><div class="count-price">$7.00</div></div>
  <div class="abs" style="left:310px;top:597px;"><div class="count">45 TENDERS</div><div class="count-price">$XX.XX</div></div>
  <div class="abs" style="left:310px;top:638px;"><div class="count">60 TENDERS</div><div class="count-price">$XX.XX</div></div>

  <div class="abs" style="left:545px;top:552px;"><div class="side-name">WAFFLE<br>FRIES</div><div class="side-size">PARTY SIZE</div><div class="side-price">$13.99</div></div>
  <div class="abs" style="left:693px;top:552px;"><div class="side-name">GARLIC<br>PARM<br>TOTS</div><div class="side-size">PARTY SIZE</div><div class="side-price">$13.99</div></div>
  <div class="abs" style="left:834px;top:552px;"><div class="side-name">CHICKEN<br>CAESAR<br>SALAD</div><div class="side-size">PARTY SIZE</div><div class="side-price">$38.99</div></div>
  <div class="abs" style="left:994px;top:552px;"><div class="side-name">CAESAR<br>SALAD</div><div class="side-size">PARTY SIZE</div><div class="side-price">$27.99</div></div>

  <div class="abs photo-plate-bl" role="img" aria-label="Platter of sauced chicken wings"></div>
  <div class="abs photo-dip" role="img" aria-label="Cup of ranch dressing"></div>
  <div class="abs photo-plate-center" role="img" aria-label="Plate of crispy chicken tenders"></div>
  <div class="abs photo-tray-br" role="img" aria-label="Tray of glazed chicken wings"></div>
  <div class="abs photo-plate-right" role="img" aria-label="Plate of buffalo wings"></div>

  <a class="abs learn-more">LEARN MORE AT <strong>BRISKETBARN-EATS.EXAMPLE/MENU</strong></a>
  <svg class="abs cursor" width="26" height="28" viewBox="0 0 26 28">
    <g stroke="#d9412f" stroke-width="2" stroke-linecap="round"><line x1="4" y1="2" x2="6" y2="6"/><line x1="0" y1="9" x2="4" y2="10"/><line x1="12" y1="0" x2="11" y2="4"/></g>
    <polygon points="8,8 24,18 17,19 21,26 18,27 14,21 9,25" fill="#d9412f" stroke="#fff" stroke-width="1.2"/>
  </svg>
</main>
</body>
</html>
```